Sales PowerPoint Template to help us attract new customers

We need to create a generic PowerPoint template for our organization. We are in the commercial facilities industry, servicing convenience, restaurants, grocery, and retail customers in the US. We handle trades such as HVAC, Refrigeration, Plumbing, Electrical, Food Equipment, Coffee, etc.

We need to incorporate our new logo, updated colors, Font (Arial). We want it to stand out in this deck and avoid looking like all other facility companies. We want to make sure the template size is not too large (less than 20 MB), so it prevent people to edit/send.
Attached are new logo, colors, old powerpoint template, and finally the "New Design to Incorporate into Template" is new materials we're looking to leverage. This might give you ideas.

Create at least 10 slides (1 cover, 1 agenda slide, at least 7 general slides, and 1 wrap-up slide)

Target Market(s)

Convenience Stores, Retail Stores, Groceries, and Restaurants in the US

Industry/Entity Type

Facilities Services (HVAC, Refrigeration, Plumbing, Electrical, etc, repair and preventative maintenance)

Font styles to use
Other font styles liked:
• Arial

Requirements
Must have
• Follow company colors and font (Arial)
Should not have
• Not approved company colors, font

```html
<!DOCTYPE html>
<html lang="en">
<head>
<meta charset="utf-8">
<title>Varnel Facility Solutions – Sales Deck Template</title>
<link rel="stylesheet" href="https://fonts.googleapis.com/css2?family=Arimo:wght@400;700&display=swap">
<style>
:root{
  --olive:#8a993b;
  --olive-dark:#4e5a1a;
  --olive-deep:#5d6a24;
  --tint:#f1f2ea;
  --ink:#333333;
  --muted:#777777;
  --white:#ffffff;
  --stage:#d7d8d1;
}
*{margin:0;padding:0;box-sizing:border-box}
html,body{width:1200px;height:2320px;overflow:hidden;background:var(--stage)}
body{font-family:"Arimo",Arial,sans-serif;color:var(--ink);position:relative}
h1,h2,h3,blockquote{font-weight:400}
.slide{position:absolute;width:510px;height:287px;background:var(--white);overflow:hidden;box-shadow:0 2px 6px rgba(0,0,0,.12)}
.slide.green{background:var(--olive);color:var(--white)}
.col-l{left:77px}.col-r{left:613px}
.r1{top:46px}.r2{top:368px}.r3{top:689px}.r4{top:1011px}.r5{top:1332px}.r6{top:1654px}.r7{top:1976px}
.abs{position:absolute}

/* brand lockup */
.brand{position:absolute;display:flex;align-items:flex-start;gap:6px;color:var(--olive)}
.brand .mark{width:14px;height:14px;background:currentColor;margin-top:2px}
.brand .name{font-size:19px;letter-spacing:4px;font-weight:400;line-height:1}
.brand .tag{font-size:8px;letter-spacing:.3px;margin-top:2px;display:block}
.brand.small{right:10px;top:8px}
.brand.small .mark{width:9px;height:9px;margin-top:1px}
.brand.small .name{font-size:12px;letter-spacing:2.5px}
.brand.small .tag{font-size:5px;margin-top:1px}
.green .brand{color:var(--white)}

.foot{position:absolute;left:13px;top:272px;font-size:5px;color:var(--muted)}
.green .foot,.green .page{color:rgba(255,255,255,.85)}
.page{position:absolute;right:14px;top:271px;font-size:6.5px;color:var(--muted)}

/* cover */
.cover-title{position:absolute;left:25px;top:139px;font-size:27px;line-height:30px;text-transform:uppercase}
.cover-title em{font-style:normal;color:var(--olive)}
.green .cover-title em{color:var(--white)}
.cover-sub{position:absolute;left:25px;top:201px;font-size:8.5px}
.cover-copy{position:absolute;left:25px;top:245px;font-size:7px}
.pill{position:absolute;left:414px;top:239px;width:64px;height:22px;border-radius:11px;background:var(--olive);color:var(--white);font-size:8px;display:flex;align-items:center;justify-content:center}
.green .pill{background:var(--white);color:var(--olive)}

/* agenda */
.agenda-title{position:absolute;left:0;right:0;top:42px;text-align:center;font-size:20px}
.agenda-title em{font-style:normal;color:var(--olive)}
.agenda-item{position:absolute;display:flex;gap:12px;align-items:center}
.num-ring{width:33px;height:33px;border:1px solid #c9cfa3;border-radius:50%;color:var(--olive);font-size:12px;display:flex;align-items:center;justify-content:center;flex:none}
.agenda-item h3{font-size:11.5px;margin-bottom:6px}
.agenda-item p{font-size:7px}

/* title + boxes */
.slide-title{position:absolute;left:34px;top:26px;font-size:20px;text-transform:uppercase}
.band{position:absolute;left:0;top:62px;width:510px;height:134px;background:var(--tint)}
.lead{position:absolute;left:29px;top:122px;width:145px;font-size:8.7px;line-height:15.5px;font-weight:700;color:var(--olive-deep)}
.stat-box{position:absolute;top:85px;width:96px;height:91px;background:var(--olive);border-radius:4px;color:var(--white);text-align:center;padding-top:12px}
.stat-box b{display:block;font-size:16px}
.stat-box strong{display:block;font-size:8.5px;margin:4px 0 5px}
.stat-box span{display:block;font-size:5.5px;line-height:9.5px;padding:0 10px}
.note{position:absolute;left:68px;top:214px;width:400px;font-size:6.8px;line-height:11.5px;color:#666}
.note-rule{position:absolute;left:58px;top:216px;width:1px;height:30px;background:var(--olive)}

/* section */
.frame{position:absolute;left:34px;top:36px;width:443px;height:216px;border:1px solid #e9e6d6}
.green .frame{border-color:rgba(255,255,255,.35)}
.section-num{position:absolute;right:51px;top:50px;font-size:78px;line-height:1;color:var(--olive)}
.green .section-num{color:var(--white)}
.section-title{position:absolute;left:49px;top:158px;font-size:30px;line-height:35px;text-transform:uppercase}
.section-title em{font-style:normal;color:var(--olive)}
.green .section-title{color:var(--olive-dark)}
.section-note{position:absolute;right:53px;top:175px;width:145px;text-align:right;font-size:7.8px;line-height:13px}

/* photo placeholders */
.photo{position:absolute}
.photo.kitchen{background:linear-gradient(135deg,#5c5148 0%,#8c6a3f 45%,#d98a2b 65%,#3d3935 100%)}
.photo.grocery{background:linear-gradient(120deg,#c9a36f 0%,#a6865f 40%,#d5864a 75%,#8e9b4c 100%)}
.photo.tech{background:linear-gradient(100deg,#4a5026 0%,#5f6436 45%,#7a7466 70%,#2f3236 100%)}

.side-head{position:absolute;left:34px;top:77px;width:130px;font-size:15.5px;line-height:18.5px;color:var(--olive-deep)}
.side-note{position:absolute;left:34px;top:180px;width:130px;font-size:5.8px;line-height:9.5px;color:#888}

/* text columns */
.col-text{position:absolute;top:59px;font-size:6.4px;line-height:10.6px}
.col-text p+p{margin-top:7px}
.col-lead{position:absolute;left:24px;top:59px;width:140px;font-size:8.4px;line-height:14px;font-weight:700;color:var(--olive)}

/* two-line title slide */
.two-title{position:absolute;left:34px;top:20px;font-size:17px;line-height:20px;color:var(--olive-dark);text-transform:uppercase}
.two-sub{position:absolute;left:34px;top:67px;width:190px;font-size:6px;line-height:10px;color:#888}
.panel{position:absolute;left:0;top:97px;width:182px;height:165px;background:var(--olive);color:var(--white);padding:26px 16px 0 34px}
.panel h3{font-size:10.5px;line-height:12.5px;margin-bottom:8px}
.panel p{font-size:5.5px;line-height:9.3px}

/* client grid */
.grid{position:absolute;inset:0;display:grid;grid-template-columns:repeat(7,1fr);grid-template-rows:repeat(6,1fr)}
.tile{background:linear-gradient(135deg,#8d8f8f,#c9c9c4)}
.tile.t2{background:linear-gradient(135deg,#4b5058,#a7a39b)}
.tile.t3{background:linear-gradient(135deg,#c9b38d,#8d8f6a)}
.tile.client{background:var(--olive);color:var(--white);font-size:5.8px;font-weight:700;display:flex;align-items:center;justify-content:center}
.tile.center{grid-column:3/6;grid-row:3/5;background:var(--white);color:var(--olive-deep);font-size:8.2px;line-height:15px;font-weight:700;text-align:center;display:flex;align-items:center;justify-content:center;padding:0 18px}

/* statement over photo */
.hero-line{position:absolute;left:49px;top:137px;width:260px;font-size:25px;line-height:28px;color:var(--white)}

/* promise */
.kicker{position:absolute;left:141px;top:56px;font-size:10.5px;color:rgba(255,255,255,.8)}
.promise{position:absolute;left:141px;top:76px;font-size:31px;line-height:36px}
.promise span{display:block}
.promise .dim{color:var(--olive-dark)}

/* quote slide */
.quote-mark{position:absolute;left:25px;top:60px;font-size:90px;line-height:1;font-weight:700;color:#e6e6e6}
.quote{position:absolute;left:65px;top:117px;width:400px;font-size:17px;line-height:24px;text-transform:uppercase;color:#444}
.cite-rule{position:absolute;left:66px;top:208px;width:2px;height:19px;background:var(--olive)}
.cite{position:absolute;left:80px;top:205px;font-size:10px}
.cite small{display:block;font-size:8.5px;color:var(--olive);margin-top:2px}

/* thank you */
.thanks{position:absolute;left:37px;top:142px;font-size:35px;font-weight:700;color:#333}
.thanks em{font-style:normal;color:var(--olive)}
.url{position:absolute;left:37px;top:195px;width:118px;height:21px;background:var(--olive);color:var(--white);font-size:8.5px;letter-spacing:.5px;display:flex;align-items:center;justify-content:center}
.brand.big{left:37px;top:34px}
</style>
</head>
<body>

<!-- Cover light -->
<section class="slide col-l r1">
  <div class="brand" style="left:25px;top:36px"><span class="mark"></span><div><span class="name">VARNEL</span><span class="tag">Facility Solutions</span></div></div>
  <h1 class="cover-title">Presentation title<br>text <em>goes here</em></h1>
  <p class="cover-sub">Lorem ipsum dolor sit amet consectetur</p>
  <p class="cover-copy">© Copyright 2025 | Varnel Facility Solutions</p>
  <span class="pill">May 2025</span>
</section>

<!-- Cover green -->
<section class="slide green col-r r1">
  <div class="brand" style="left:25px;top:36px"><span class="mark"></span><div><span class="name">VARNEL</span><span class="tag">Facility Solutions</span></div></div>
  <h1 class="cover-title" style="color:var(--olive-dark)">Presentation title<br>text <em>goes here</em></h1>
  <p class="cover-sub">Lorem ipsum dolor sit amet consectetur</p>
  <p class="cover-copy">© Copyright 2025 | Varnel Facility Solutions</p>
  <span class="pill">May 2025</span>
</section>

<!-- Agenda -->
<section class="slide col-l r2">
  <div class="brand small"><span class="mark"></span><div><span class="name">VARNEL</span><span class="tag">Facility Solutions</span></div></div>
  <h2 class="agenda-title">OUR <em>AGENDA</em></h2>
  <div class="agenda-item" style="left:34px;top:91px"><span class="num-ring">01</span><div><h3>Subtitle Text Here</h3><p>Lorem ipsum dolor sit amet dummy texts</p></div></div>
  <div class="agenda-item" style="left:34px;top:149px"><span class="num-ring">02</span><div><h3>Subtitle Text Here</h3><p>Lorem ipsum dolor sit amet dummy texts</p></div></div>
  <div class="agenda-item" style="left:34px;top:205px"><span class="num-ring">03</span><div><h3>Subtitle Text Here</h3><p>Lorem ipsum dolor sit amet dummy texts</p></div></div>
  <div class="agenda-item" style="left:264px;top:91px"><span class="num-ring">04</span><div><h3>Subtitle Text Here</h3><p>Lorem ipsum dolor sit amet dummy texts</p></div></div>
  <div class="agenda-item" style="left:264px;top:149px"><span class="num-ring">05</span><div><h3>Subtitle Text Here</h3><p>Lorem ipsum dolor sit amet dummy texts</p></div></div>
  <div class="agenda-item" style="left:264px;top:205px"><span class="num-ring">06</span><div><h3>Subtitle Text Here</h3><p>Lorem ipsum dolor sit amet dummy texts</p></div></div>
  <p class="foot">© Copyright 2025 | Varnel Facility Solutions</p><span class="page">02</span>
</section>

<!-- Title + description boxes -->
<section class="slide col-r r2">
  <div class="brand small"><span class="mark"></span><div><span class="name">VARNEL</span><span class="tag">Facility Solutions</span></div></div>
  <h2 class="slide-title">Enter title here</h2>
  <div class="band"></div>
  <svg class="abs" style="left:29px;top:81px" width="20" height="26" viewBox="0 0 20 26" aria-hidden="true">
    <rect x="1" y="1" width="12" height="16" rx="1.5" fill="none" stroke="#8a993b" stroke-width="2.2"/>
    <path d="M4 6h6M4 10h6" stroke="#8a993b" stroke-width="2"/>
    <path d="M3 24l6-6h6l4-4" fill="none" stroke="#8a993b" stroke-width="2.4" stroke-linecap="round"/>
  </svg>
  <p class="lead">Lorem ipsum dolor sit amet dummy texts. Duis quis amet nunc vulputate dolor. Sceler ligula velit nulla faucibus</p>
  <div class="stat-box" style="left:184px"><b>01</b><strong>Description</strong><span>Lorem ipsum dolor sit amet dummy texts. Duis quis amet nunc</span></div>
  <div class="stat-box" style="left:289px"><b>02</b><strong>Description</strong><span>Lorem ipsum dolor sit amet dummy texts. Duis quis amet nunc</span></div>
  <div class="stat-box" style="left:392px"><b>03</b><strong>Description</strong><span>Lorem ipsum dolor sit amet dummy texts. Duis quis amet nunc</span></div>
  <svg class="abs" style="left:29px;top:222px" width="20" height="20" viewBox="0 0 20 20" aria-hidden="true">
    <rect x="1" y="12" width="3.5" height="7" fill="#8a993b"/><rect x="6.5" y="9" width="3.5" height="10" fill="#8a993b"/><rect x="12" y="11" width="3.5" height="8" fill="#8a993b"/>
    <path d="M1 9l6-5 5 3 6-6" fill="none" stroke="#8a993b" stroke-width="1.8"/>
  </svg>
  <span class="note-rule"></span>
  <p class="note">Lorem ipsum dolor sit amet dummy texts. Duis quis amet nunc vulputate dolor. Scelerisque ligula velit nulla faucibus donec pellentesque massa mi. Aliquam in fusce semper aliquam egestas mauris est nunc. Et pellentesque sodales elementum cursus mattis suscipit etiam nulla odio. Molestie tristique cursus</p>
  <p class="foot">© Copyright 2025 | Varnel Facility Solutions</p><span class="page">02</span>
</section>

<!-- Section 01 -->
<section class="slide col-l r3">
  <div class="brand small"><span class="mark"></span><div><span class="name">VARNEL</span><span class="tag">Facility Solutions</span></div></div>
  <div class="frame"></div>
  <span class="section-num">01</span>
  <h2 class="section-title">Section<br><em>Slides</em></h2>
  <p class="section-note">Lorem ipsum dolor sit amet dummy texts. Duis quis amet nunc vulputate dolor scelerisque ligula.</p>
  <p class="foot">© Copyright 2025 | Varnel Facility Solutions</p><span class="page">02</span>
</section>

<!-- Section 02 -->
<section class="slide green col-r r3">
  <div class="brand small"><span class="mark"></span><div><span class="name">VARNEL</span><span class="tag">Facility Solutions</span></div></div>
  <div class="frame"></div>
  <span class="section-num">02</span>
  <h2 class="section-title">Section<br>Slides</h2>
  <p class="section-note">Lorem ipsum dolor sit amet dummy texts. Duis quis amet nunc vulputate dolor scelerisque ligula.</p>
  <p class="foot">© Copyright 2025 | Varnel Facility Solutions</p><span class="page">02</span>
</section>

<!-- Photo split -->
<section class="slide col-l r4">
  <div class="photo kitchen" style="left:165px;top:0;width:345px;height:287px" role="img" aria-label="Chef flambéing a pan in a commercial restaurant kitchen"></div>
  <div class="brand small"><span class="mark"></span><div><span class="name">VARNEL</span><span class="tag">Facility Solutions</span></div></div>
  <h2 class="side-head">Lorem ipsum dolor sit amet dummy texts. Duissuis amet nunces sets</h2>
  <p class="side-note">Lorem ipsum dolor sit amet dummy texts. Duis quis amet nunc vulputate dolor. Scelerisque ligula velit nulla fauci donec.</p>
  <p class="foot">© Copyright 2025 | Varnel Facility Solutions</p>
</section>

<!-- Text columns -->
<section class="slide col-r r4">
  <div class="brand small"><span class="mark"></span><div><span class="name">VARNEL</span><span class="tag">Facility Solutions</span></div></div>
  <p class="col-lead">Lorem ipsum dolor sit amet dummy texts. Duis quis amet nu vulputate dolor. Sceleri ligula velit nulla faucibus donec pellentesque massa miesat. Aliquam in fusce semper aliqua egestas mauris est nunc.</p>
  <div class="col-text" style="left:200px;width:128px">
    <p>Lorem ipsum dolor sit amet dummy texts. Duis quis amet nunc vulputate dolor. Scelerisque ligula velit nulla fauci donec pellentesque massa mi. Aliquam in fusce semper aliquam egestas mauris est nunc. Et pellentese sodales elementum cursus mattis suscipit etiam.</p>
    <p>Molestie tristique cursus ipsum non vitae nibh amet lacus. Orci dictum erat vitae at at non massa. Sit sit nisl pretium quisque ornare nunc posuere nunc. Et at est varius pulvinar sodales massa pulvinar risus. Orci at ipsum tellus posuere nunc. Auctor malesuada plac.</p>
  </div>
  <div class="col-text" style="left:339px;width:130px">
    <p>Eget libero aliquet hendrerit et tellus aliquam enim proin elementum. Enim purus nulla nunc accumsan suspen disse gravida dolor nulla. Eget diam elit rhoncus dui integer egestas. Eget sagittis tortor arcu id nec eu integer morbi risus posuere egestas ac.</p>
    <p>Penatibus imperdiet adipiscing rhoncus blandit tortor in. Tortor sagittis massa adipiscing in at nam placerat tincidunt. Ut interdum integer senectus a sapien. Tortor magna velit ut non. Tellus massa etiam vel elementum varius in leo. Vitae id magna laoreet mauris.</p>
  </div>
  <p class="foot">© Copyright 2025 | Varnel Facility Solutions</p><span class="page">02</span>
</section>

<!-- Two-line title -->
<section class="slide col-l r5">
  <div class="brand small"><span class="mark"></span><div><span class="name">VARNEL</span><span class="tag">Facility Solutions</span></div></div>
  <h2 class="two-title">Enter your two-line<br>title here</h2>
  <p class="two-sub">Lorem ipsum dolor sit amet dummy texts. Duis quis amet nunc vulputate dolor. Scelerisque ligula velit nulla fauci donec.</p>
  <div class="panel">
    <h3>Lorem ipsum dolor sit amet dummy texts duis</h3>
    <p>Lorem ipsum dolor sit amet dummy texts. Duis quis amet nunc vulputate dolor. Scelerisque ligula velit nulla faucibus donec pellentesque massa mi. Aliquam in fusce semper aliquam egestas mauris est nunc. Et pellentesque soda elementum cursus mattis suscipit etiam nulla odio. Molestie tristique cursus ipsum non vitae nibh amet lacus orci dictum erat</p>
  </div>
  <div class="photo grocery" style="left:182px;top:97px;width:328px;height:165px" role="img" aria-label="Family shopping for fresh produce in a grocery store"></div>
  <p class="foot">© Copyright 2025 | Varnel Facility Solutions</p><span class="page">02</span>
</section>

<!-- Client grid -->
<section class="slide col-r r5">
  <div class="grid">
    <div class="tile t2" role="img" aria-label="Commercial kitchen equipment"></div><div class="tile client">Client Name</div><div class="tile" role="img" aria-label="Restaurant kitchen"></div><div class="tile t2" role="img" aria-label="Technician at work"></div><div class="tile client">Client Name</div><div class="tile" role="img" aria-label="Plumbing fittings"></div><div class="tile client">Client Name</div>
    <div class="tile t3" role="img" aria-label="Cups on a counter"></div><div class="tile t2" role="img" aria-label="Retail store interior"></div><div class="tile client">Client Name</div><div class="tile t2" role="img" aria-label="Technician with safety glasses"></div><div class="tile" role="img" aria-label="Cooking range"></div><div class="tile client">Client Name</div><div class="tile t3" role="img" aria-label="Grocery shelves"></div>
    <div class="tile client">Client Name</div><div class="tile" role="img" aria-label="Technician servicing equipment"></div><div class="tile center">Lorem ipsum dolor sit amet dummy texts. Duis quis amet nu vulputate dolor. Sceleri ligula velit nulla faucibus donec pellentesque massa miesat.</div><div class="tile t2" role="img" aria-label="Refrigeration repair"></div><div class="tile t3" role="img" aria-label="Technician in hi-vis vest"></div>
    <div class="tile t2" role="img" aria-label="Electrical panel work"></div><div class="tile client">Client Name</div><div class="tile t3" role="img" aria-label="Cups on a counter"></div><div class="tile client">Client Name</div>
    <div class="tile t3" role="img" aria-label="Produce display"></div><div class="tile t2" role="img" aria-label="Stove burners"></div><div class="tile client">Client Name</div><div class="tile" role="img" aria-label="Technician at a control box"></div><div class="tile t2" role="img" aria-label="Kitchen equipment"></div><div class="tile client">Client Name</div><div class="tile t3" role="img" aria-label="Grocery aisle"></div>
    <div class="tile client">Client Name</div><div class="tile t2" role="img" aria-label="Technician with hard hat"></div><div class="tile" role="img" aria-label="Plumbing fittings"></div><div class="tile client">Client Name</div><div class="tile" role="img" aria-label="Commercial kitchen"></div><div class="tile t2" role="img" aria-label="Technician servicing equipment"></div><div class="tile t3" role="img" aria-label="Technician at work"></div>
  </div>
</section>

<!-- Full photo statement -->
<section class="slide col-l r6">
  <div class="photo tech" style="inset:0" role="img" aria-label="Electrician in hard hat and safety glasses working at an electrical panel"></div>
  <h2 class="hero-line">Lorem ipsum dolor sit amet dummy texts. Duissuis amet nunces sets</h2>
</section>

<!-- Promise -->
<section class="slide green col-r r6">
  <div class="brand small"><span class="mark"></span><div><span class="name">VARNEL</span><span class="tag">Facility Solutions</span></div></div>
  <p class="kicker">OUR PROMISE:</p>
  <h2 class="promise"><span>Spend less.</span><span>Strees less.</span><span class="dim">One work order</span><span class="dim">at a time.</span></h2>
  <p class="foot">© Copyright 2025 | Varnel Facility Solutions</p><span class="page">02</span>
</section>

<!-- Quote -->
<section class="slide col-l r7">
  <div class="brand small"><span class="mark"></span><div><span class="name">VARNEL</span><span class="tag">Facility Solutions</span></div></div>
  <span class="quote-mark" aria-hidden="true">“</span>
  <blockquote class="quote">Lorem ipsum dolor sit amet dummy texts. Duis quis amet nunc vultate dolor scelerisque ligula.</blockquote>
  <span class="cite-rule"></span>
  <p class="cite">Dr. Dana Morrow<small>CEO / Founder</small></p>
  <p class="foot">© Copyright 2025 | Varnel Facility Solutions</p><span class="page">02</span>
</section>

<!-- Thank you -->
<section class="slide col-r r7">
  <div class="brand big"><span class="mark"></span><div><span class="name">VARNEL</span><span class="tag">Facility Solutions</span></div></div>
  <h2 class="thanks">THANK <em>YOU</em></h2>
  <span class="url">www.varnelurl.com</span>
</section>

</body>
</html>
```